Start up in business consultancy needs a business card

We need the business card's layout (we have already the logo). Our business is concerned on consultancy services delivered to companies on the matter of sustainability. Business card should be enough essentials and professional style.

Side A with the following info:
logo + a space for the claim (still to identify) + website of the company

Side B with the following info:
Name of business card holder + title of the business card holder + address of the company + space for mobile number, phone number, fax number + e-mail of business card holder + graphic details around.

Target Market(s)

Business of any sector

Industry/Entity Type

Business Service

Contact Information for Business Card

Name of the company:
Pianoverde srl
Società Benefit

Address of the company:
Via Lucerna, 7
21047 - Saronno (VA)

Website:
www.pianoverde.it

Name of the BC' holder:
Luca Ferentino

Title:
Co-fondatore

Email:
luca@pianoverde.it

Mobile:
+39 348 915 2074
Phone:
+39 348 915 2074
Fax:
+39 348 915 2074

Font styles to use
Other font styles liked:
• new gothic

```html
<!DOCTYPE html>
<html lang="it">
<head>
<meta charset="utf-8">
<title>Pianoverde – biglietto da visita</title>
<link rel="stylesheet" href="https://fonts.googleapis.com/css2?family=Oswald:wght@500;600&family=Montserrat:wght@400;500&family=Arimo:wght@400&display=swap">
<style>
  :root{
    --brand-blue:#1565ad;
    --brand-blue-faint:#e6eef7;
    --paper:#ffffff;
    --ink:#333a40;
    --backdrop:#2b2c2e;
    --dots:#2a2a2a;
  }
  *{box-sizing:border-box;margin:0;padding:0}
  html,body{width:1200px;height:900px;overflow:hidden;background:var(--backdrop)}
  .canvas{
    width:1200px;height:900px;
    display:flex;flex-direction:column;align-items:center;justify-content:center;gap:40px;
  }
  .card{
    position:relative;width:660px;height:377px;
    background:var(--paper);border-radius:22px;overflow:hidden;
    box-shadow:0 10px 30px rgba(0,0,0,.45);
  }
  .wordmark{
    font-family:"Montserrat",sans-serif;font-weight:500;letter-spacing:.5px;
  }

  /* front side */
  .front .faint-ring{position:absolute;left:-120px;top:150px}
  .front .brand{
    position:absolute;left:250px;top:48px;display:flex;align-items:center;gap:14px;
  }
  .front .brand .wordmark{font-size:34px;color:var(--brand-blue)}
  .front .legal-form{
    position:absolute;right:70px;top:118px;
    font-family:"Oswald",sans-serif;font-weight:600;font-size:17px;
    color:var(--brand-blue);letter-spacing:.5px;text-transform:uppercase;
  }
  .front .claim-line{
    position:absolute;left:110px;right:70px;border-top:2px dotted var(--dots);
  }
  .front .claim-line.first{top:188px}
  .front .claim-line.second{top:246px}
  .front .website{
    position:absolute;left:0;right:0;top:296px;text-align:center;
    font-family:"Arimo",sans-serif;font-size:16px;color:var(--ink);
  }
  .front .website .domain{color:var(--brand-blue)}

  /* back side */
  .back .disc{position:absolute;left:0;top:0}
  .back .edge-strip{
    position:absolute;left:12px;top:168px;width:6px;height:170px;background:var(--paper);
  }
  .back .ring-mark{position:absolute;right:72px;top:50px}
  .back .holder{
    position:absolute;left:38px;top:110px;color:var(--paper);
  }
  .back .holder .wordmark{font-size:34px;margin-bottom:14px;display:block}
  .back .name{
    font-family:"Oswald",sans-serif;font-weight:600;font-size:19px;text-transform:uppercase;letter-spacing:.3px;
    display:block;margin-left:34px;line-height:1.1;
  }
  .back .role,.back .address,.back .contacts{
    font-family:"Arimo",sans-serif;font-size:15px;margin-left:34px;
  }
  .back .role{margin-bottom:18px;display:block}
  .back .address{font-style:normal;line-height:1.3;margin-bottom:16px}
  .back .contacts{list-style:none;line-height:1.45}
  .back .contacts li{display:flex;align-items:center;gap:10px}
  .back .contacts svg{width:14px;height:14px;flex:none}
</style>
</head>
<body>
<main class="canvas">

  <section class="card front" aria-label="Fronte">
    <svg class="faint-ring" width="330" height="330" viewBox="0 0 330 330" aria-hidden="true">
      <circle cx="165" cy="165" r="150" fill="none" stroke="var(--brand-blue-faint)" stroke-width="14"/>
    </svg>
    <div class="brand">
      <svg width="58" height="58" viewBox="0 0 58 58" aria-hidden="true">
        <circle cx="29" cy="29" r="26" fill="none" stroke="var(--brand-blue)" stroke-width="4"/>
      </svg>
      <span class="wordmark">pianoverde</span>
    </div>
    <p class="legal-form">Società Benefit</p>
    <div class="claim-line first"></div>
    <div class="claim-line second"></div>
    <p class="website">www.<span class="domain">pianoverde</span>.it</p>
  </section>

  <section class="card back" aria-label="Retro">
    <svg class="disc" width="660" height="377" viewBox="0 0 660 377" aria-hidden="true">
      <circle cx="170" cy="330" r="290" fill="var(--brand-blue)"/>
      <circle cx="170" cy="330" r="304" fill="none" stroke="var(--brand-blue)" stroke-width="4"/>
    </svg>
    <svg class="ring-mark" width="150" height="150" viewBox="0 0 150 150" aria-hidden="true">
      <circle cx="75" cy="75" r="68" fill="none" stroke="var(--brand-blue)" stroke-width="6"/>
    </svg>
    <div class="edge-strip"></div>

    <div class="holder">
      <span class="wordmark">pianoverde</span>
      <span class="name">Luca Ferentino</span>
      <span class="role">Co-fondatore</span>
      <address class="address">Via Lucerna, 7<br>21047 - Saronno (VA)</address>
      <ul class="contacts">
        <li>
          <svg viewBox="0 0 14 14" aria-label="Cellulare"><rect x="3.5" y="1" width="7" height="12" rx="1.2" fill="none" stroke="currentColor" stroke-width="1.4"/><circle cx="7" cy="11" r=".8" fill="currentColor"/></svg>
          +39 348 915 2074
        </li>
        <li>
          <svg viewBox="0 0 14 14" aria-label="Telefono"><path d="M3 1.5l2.2 2.6-1.2 1.5c.8 1.8 2.3 3.3 4.1 4.1l1.5-1.2 2.6 2.2-1.4 1.8C6 12.4 1.6 8 1.2 2.9z" fill="currentColor"/></svg>
          +39 348 915 2074
        </li>
        <li>
          <svg viewBox="0 0 14 14" aria-label="Fax"><rect x="3.5" y="1" width="7" height="4" fill="currentColor"/><rect x="1" y="6" width="12" height="5" rx="1" fill="currentColor"/><rect x="3.5" y="10" width="7" height="3" fill="currentColor"/></svg>
          +39 348 915 2074
        </li>
        <li>
          <svg viewBox="0 0 14 14" aria-label="E-mail"><rect x="1" y="3" width="12" height="8.5" fill="none" stroke="currentColor" stroke-width="1.3"/><path d="M1.5 3.5L7 8l5.5-4.5" fill="none" stroke="currentColor" stroke-width="1.3"/></svg>
          luca@pianoverde.it
        </li>
      </ul>
    </div>
  </section>

</main>
</body>
</html>
```